Modern Label for Loose Tea pouches on 4.5x6 Label

We need a new label for our teas that is very simple in design, but stylish and modern. This will be used to print labels for our loose tea pouches. The label will be at max 4.5x6 inches in size. There should be a place for the tea name, description, ingredients, and size that is changeable.
Preferably an AI file that allows me to setup variables to change the above items. There will also need to be our logo which is supplied, and our address on the label.
Address:
Brevo Leaf
846 Lower Maple Lane
Fernbrook, VT 05617
Target Market(s)
Tea Lovers
Requirements
Must have
- Adobe Illustrator file with variables setup for replacement of tea name, description, ingredients, and size (weights 2oz, 4oz, 8oz, 1lb)

```html
<!DOCTYPE html>
<html lang="en">
<head>
<meta charset="utf-8">
<title>Brevo Leaf – Loose Tea Label</title>
<link rel="stylesheet" href="https://fonts.googleapis.com/css2?family=Pinyon+Script&family=Roboto:wght@300;400;500&family=Roboto+Condensed:wght@400&display=swap">
<style>
  :root {
    --canvas: #ffffff;
    --frame-line: #c8c8c8;
    --tea-pink: #e0509f;
    --leaf-green: #9fcf4a;
    --label-edge: #b7dc8a;
    --pattern-pink: #f3858b;
    --pattern-soft: #f7a4a6;
    --ink: #333333;
    --ink-dark: #111111;
  }
  * { margin: 0; padding: 0; box-sizing: border-box; }
  html, body {
    width: 1200px; height: 1000px; overflow: hidden;
    background: var(--canvas);
  }
  .artboard { position: relative; width: 1200px; height: 1000px; }
  .print-frame {
    position: absolute; left: 407px; top: 215px;
    width: 321px; height: 387px;
    border: 1px solid var(--frame-line);
  }
  .label {
    position: absolute; left: 437px; top: 241px;
    width: 261px; height: 333px;
    border-right: 1px solid var(--label-edge);
    border-left: 1px solid #e6e6e6;
    background: #fff;
    overflow: hidden;
  }
  .pattern-band {
    position: absolute; left: 0; width: 260px;
    background: linear-gradient(90deg, var(--pattern-pink), var(--pattern-soft) 50%, var(--pattern-pink));
  }
  .pattern-band--top { top: 0; height: 7px; }
  .pattern-band--bottom { bottom: 0; height: 39px; }
  .tea-name {
    position: absolute; left: 0; width: 260px; top: 10px;
    text-align: center; white-space: nowrap;
    font-family: "Pinyon Script", cursive; font-weight: 400;
    font-size: 38px; line-height: 44px; letter-spacing: 1px;
    color: var(--tea-pink);
  }
  .tea-description {
    position: absolute; left: 0; width: 260px; top: 51px;
    text-align: center; white-space: nowrap;
    font-family: "Roboto", sans-serif; font-weight: 300;
    font-size: 19px; line-height: 22px;
    color: var(--leaf-green);
  }
  .divider { position: absolute; left: 0; top: 78px; }
  .net-weight {
    position: absolute; left: 0; width: 252px; top: 90px;
    text-align: center;
    font-family: "Roboto", sans-serif; font-weight: 300;
    font-size: 14px; letter-spacing: 0.5px; color: var(--ink);
  }
  .ingredients {
    position: absolute; left: 0; width: 250px; top: 115px;
    text-align: center;
    font-family: "Roboto", sans-serif; font-weight: 400;
    font-size: 9px; color: var(--ink);
  }
  .brand-mark {
    position: absolute; left: 0; width: 260px; top: 242px;
    display: flex; align-items: center; justify-content: center; gap: 8px;
  }
  .brand-mark__dot {
    width: 14px; height: 14px; border-radius: 50%;
    background: var(--leaf-green);
  }
  .brand-mark__name {
    font-family: "Roboto", sans-serif; font-weight: 500;
    font-size: 19px; letter-spacing: 2px;
    color: var(--tea-pink);
  }
  .address {
    position: absolute; left: 0; width: 260px; top: 275px;
    text-align: center; white-space: nowrap;
    font-family: "Roboto Condensed", sans-serif; font-weight: 400;
    font-size: 12px; letter-spacing: -0.4px;
    color: var(--ink-dark);
  }
</style>
</head>
<body>
<main class="artboard">
  <div class="print-frame"></div>
  <section class="label">
    <div class="pattern-band pattern-band--top" role="img" aria-label="Pink floral lattice pattern border"></div>

    <h1 class="tea-name">Tea Name</h1>
    <p class="tea-description">Description of the tea name.</p>

    <svg class="divider" width="260" height="10" viewBox="0 0 260 10" aria-hidden="true">
      <line x1="32" y1="2" x2="231" y2="2" stroke="var(--tea-pink)" stroke-width="1.5"/>
      <line x1="47" y1="6" x2="219" y2="6" stroke="var(--tea-pink)" stroke-width="1.5"/>
    </svg>

    <p class="net-weight">Net. Wt.</p>
    <p class="ingredients">Ingredients</p>

    <div class="brand-mark">
      <span class="brand-mark__dot"></span>
      <span class="brand-mark__name">BREVO LEAF</span>
    </div>

    <p class="address">Brevo Leaf&nbsp;&nbsp; 846 Lower Maple Lane Fernbrook, VT 05617</p>

    <div class="pattern-band pattern-band--bottom" role="img" aria-label="Pink floral lattice pattern border"></div>
  </section>
</main>
</body>
</html>
```